Special Educational Conference Poster

Looking for a poster that I can use electronically more than anything - to post on Chatterbook \ social media. Should be bold, eye catching, and within our brand colors.

3rd Annual Young Learners Beyond Limits Summit
Featuring Dr. Martin Ellery
Lighting the Way: Growing Courage, Drive, and Grit in Every Young Learner Who Thinks Differently

Friday, May 10, 2019, 9am - 3pm

The Linden Grove Academy at Fenwick opens our campus to teachers, parents, and practitioners from the Delaware Valley to learn together on how to support the extraordinary students in our lives. The conference runs from 9am - 3pm and lunch is included. This event is free and open to the public, but registration is required.

Link to registration: https://www.lindengroveacad.org/admissions/admissions-visit-and-events

```html
<!DOCTYPE html>
<html lang="en">
<head>
<meta charset="utf-8">
<title>3rd Annual Young Learners Beyond Limits Summit</title>
<link rel="stylesheet" href="https://fonts.googleapis.com/css2?family=Open+Sans:wght@600;700&family=Oswald:wght@500;600&display=swap">
<style>
  :root {
    --page: #e9e4dc;
    --sky-top: #1b2f48;
    --sky-mid: #3d5d7c;
    --night: #050608;
    --ink: #ffffff;
    --rule: #e6e6e6;
    --portrait-light: #c9c2bb;
    --portrait-dark: #1d2a44;
    --crest: #8fa3bb;
  }
  * { margin: 0; padding: 0; box-sizing: border-box; }
  html, body { width: 1200px; height: 1200px; overflow: hidden; background: var(--page); }
  .poster {
    position: absolute; left: 190px; top: 20px;
    width: 820px; height: 1160px; overflow: hidden;
    color: var(--ink);
    font-family: "Oswald", "Arial Narrow", sans-serif;
  }
  .poster-backdrop {
    position: absolute; inset: 0;
    background: linear-gradient(180deg, var(--sky-top) 0%, #2a4663 22%, var(--sky-mid) 38%, #1e2d3c 50%, #0b0e12 60%, var(--night) 72%);
  }
  .event-title {
    position: absolute; left: 0; top: 68px; width: 820px;
    text-align: center;
    font-family: "Open Sans", Arial, sans-serif; font-weight: 600;
    font-size: 41px; line-height: 56px;
  }
  .title-rule {
    position: absolute; left: 59px; top: 239px; width: 696px; height: 3px;
    background: var(--rule);
  }
  .theme {
    position: absolute; left: 0; top: 262px; width: 820px;
    text-align: center; font-weight: 500; font-size: 21px; line-height: 32px;
  }
  .event-date {
    position: absolute; left: 517px; top: 660px; width: 254px;
    text-align: center; font-weight: 600;
  }
  .event-date .day { font-size: 43px; line-height: 56px; }
  .event-date .date { font-size: 48px; line-height: 58px; }
  .event-date .date-rule { height: 4px; background: var(--rule); margin: 6px 0 8px; }
  .event-date .time { font-size: 31px; line-height: 38px; }
  .speaker {
    position: absolute; left: 21px; top: 750px;
    font-weight: 600; font-size: 24px; line-height: 38px;
  }
  .speaker-portrait {
    position: absolute; left: 6px; top: 831px; width: 361px; height: 329px;
    background: linear-gradient(180deg, var(--portrait-light) 0%, #9c8f86 45%, var(--portrait-dark) 80%);
  }
  .registration {
    position: absolute; left: 359px; top: 914px; width: 421px;
  }
  .registration .label {
    text-align: center; font-weight: 600; font-size: 34px; line-height: 46px;
  }
  .registration .label-rule { height: 4px; background: var(--rule); margin: 10px 0 8px; }
  .registration .url {
    text-align: right; font-weight: 500; font-size: 19px; line-height: 30px;
  }
  .school-name {
    position: absolute; right: 40px; top: 1070px; width: 220px;
    text-align: right; color: var(--crest);
    font-family: "Open Sans", Arial, sans-serif; font-weight: 600;
    font-size: 15px; line-height: 20px;
  }
</style>
</head>
<body>
  <main class="poster">
    <div class="poster-backdrop" role="img" aria-label="Starry night sky over mountains, with silhouettes of children reading under a tree and climbers helping each other up a hill"></div>

    <h1 class="event-title">3rd Annual Young Learners<br>Beyond Limits Summit</h1>
    <div class="title-rule"></div>

    <p class="theme">Lighting the Way:<br>Growing Courage, Drive, and Grit in Every<br>Young Learner Who Thinks Differently</p>

    <div class="event-date">
      <div class="day">Friday</div>
      <div class="date">May 10, 2019</div>
      <div class="date-rule"></div>
      <div class="time">9am - 3pm</div>
    </div>

    <p class="speaker">Featuring,<br>Dr. Martin Ellery</p>
    <div class="speaker-portrait" role="img" aria-label="Portrait photograph of the featured speaker, Dr. Martin Ellery"></div>

    <div class="registration">
      <div class="label">Link to registration :</div>
      <div class="label-rule"></div>
      <div class="url">https://www.lindengroveacad.org/admissions<br>/admissions-visit-and-events</div>
    </div>

    <p class="school-name">The Linden Grove Academy<br>at Fenwick</p>
  </main>
</body>
</html>
```